Flyer Design for Private Car Service

Flyer should cater to Business Travelers and Executives who travel Business Class or First Class.
Flyer should include images attached.
Flyer should include the below text
Dallas to Austin
Chauffeured SUVs
• Travel Dallas to Austin in a new 2025 Marlow Strider for $499 one-way
• Trip includes a Uniformed Chauffeur who has a Commercial Drivers License (CDL)
• You can Schedule Chauffeur Pickup at Your Home in Dallas
• Our Chauffeur will Drop You Off at Your Final Destination in Austin
• You can Schedule Chauffeur Return Pickup in Austin and Return Back to Dallas.
• We offer Faster Times on Door-to-Door Travel than Bluecrest Airways
• We offer Comparable Prices on Door-to-Door Travel Times than Bluecrest Airways
• All of our trips are insured with $500k of commercial auto insurance
• Our Passengers can Talk on Cell Phone & Conduct Quill calls Throughout Travel
• Our Passengers have Maximum Privacy, Comfort and First-Class Amenities.
• Our Passengers Avoid Harwick Vale Field and KPR Airport hassles & delays
• Member Brenton Chamber of Commerce, Larkmoor Chamber of Commerce.
• Book your trip today at www.ridemarquel.example
Target Market(s)
Business Travelers
Look and feel
Each slider illustrates characteristics of the customer's brand and the style your logo design should communicate.

```html
<!DOCTYPE html>
<html lang="en">
<head>
<meta charset="utf-8">
<title>Dallas to Austin – Chauffeured SUVs</title>
<link href="https://fonts.googleapis.com/css2?family=Barlow+Condensed:ital,wght@1,700&family=Jost:ital,wght@0,300;0,400;0,600;1,300&display=swap" rel="stylesheet">
<style>
  :root {
    --red: #e41e2b;
    --ink: #1b1b1b;
    --black: #141414;
    --white: #ffffff;
    --mist: #f1f1f1;
  }
  * { margin: 0; padding: 0; box-sizing: border-box; }
  html, body { width: 848px; height: 1200px; overflow: hidden; background: var(--white); }
  .flyer {
    position: relative; width: 848px; height: 1200px; overflow: hidden;
    background: var(--white); font-family: "Jost", sans-serif; color: var(--ink);
  }
  .hero-photo {
    position: absolute; left: 0; top: 0; width: 848px; height: 470px;
    background:
      linear-gradient(180deg, rgba(255,255,255,1) 0%, rgba(255,255,255,0.9) 30%, rgba(255,255,255,0) 45%, rgba(255,255,255,0) 85%, rgba(255,255,255,1) 100%),
      linear-gradient(90deg, #2a2a2a 0%, #4a4a4a 22%, #dcdcdc 45%, #e9e9e9 55%, #c8232c 75%, #d42a32 100%);
  }
  .brand {
    position: absolute; top: 28px; left: 0; width: 848px; text-align: center;
  }
  .brand-mark {
    width: 52px; height: 52px; border-radius: 50%; background: var(--red);
    margin: 0 auto 22px;
  }
  .brand-name {
    font-weight: 400; font-size: 46px; letter-spacing: 6px; color: var(--ink);
  }
  .headline {
    position: absolute; top: 432px; left: 0; width: 848px; text-align: center;
    font-family: "Barlow Condensed", sans-serif; font-style: italic; font-weight: 700;
    font-size: 66px; line-height: 1; color: var(--black); letter-spacing: 0.5px;
  }
  .headline .accent { color: var(--red); }
  .swoosh { position: absolute; left: 0; top: 496px; width: 848px; height: 40px; }
  .subhead {
    position: absolute; top: 526px; left: 0; width: 848px; text-align: center;
    font-weight: 300; font-style: italic; font-size: 58px; line-height: 1; color: var(--ink);
  }
  .features {
    position: absolute; top: 614px; left: 42px; width: 764px; list-style: none;
  }
  .features li {
    height: 34.3px; line-height: 31px; text-align: center; font-size: 15.6px;
    font-weight: 400; text-transform: uppercase; white-space: nowrap;
    border-bottom: 2px solid var(--red);
  }
  .features strong { font-weight: 600; }
  .footer { position: absolute; left: 0; top: 1060px; width: 848px; height: 140px; }
  .footer-band { position: absolute; inset: 0; }
  .footer-pin { position: absolute; left: 134px; top: -14px; width: 74px; height: 108px; }
  .cta {
    position: absolute; left: 207px; top: 58px;
    font-family: "Barlow Condensed", sans-serif; font-style: italic; font-weight: 700;
    font-size: 29px; color: var(--white); text-transform: uppercase; white-space: nowrap;
  }
  .cta .url { color: var(--red); }
</style>
</head>
<body>
<div class="flyer">
  <div class="hero-photo" role="img" aria-label="Four uniformed chauffeurs standing beside black, white and red SUVs in front of a building"></div>

  <header class="brand">
    <div class="brand-mark"></div>
    <div class="brand-name">MARQUEL</div>
  </header>

  <h1 class="headline"><span class="accent">DALLAS</span> TO <span class="accent">AUSTIN</span></h1>

  <svg class="swoosh" viewBox="0 0 848 40" preserveAspectRatio="none" aria-hidden="true">
    <path d="M0 30 Q424 -4 848 30 L848 36 Q424 4 0 36 Z" fill="var(--red)"/>
  </svg>

  <h2 class="subhead">CHAUFFEURED SUVS</h2>

  <ul class="features">
    <li>Travel Dallas to Austin in a new 2025 Marlow Strider for <strong>$499 one-way</strong></li>
    <li>Trip includes a uniformed chauffeur who has a commercial drivers license (CDL)</li>
    <li>You can schedule chauffeur pickup at your home in Dallas</li>
    <li>Our chauffeur will drop you off at your final destination in Austin</li>
    <li>You can schedule chauffeur return pickup in Austin and return back to Dallas.</li>
    <li>We offer faster times on door-to-door travel than Bluecrest Airways</li>
    <li>We offer comparable prices on door-to-door travel times than Bluecrest Airways</li>
    <li>All of our trips are insured with <strong>$500K</strong> of commercial auto insurance</li>
    <li>Our passengers can talk on cell phone &amp; conduct Quill calls throughout travel</li>
    <li>Our passengers have maximum privacy, comfort and first-class amenities.</li>
    <li>Our passengers avoid Harwick Vale Field and KPR Airport hassles &amp; delays</li>
    <li>Member Brenton Chamber of Commerce, Larkmoor Chamber of Commerce.</li>
  </ul>

  <footer class="footer">
    <svg class="footer-band" viewBox="0 0 848 140" preserveAspectRatio="none" aria-hidden="true">
      <path d="M0 44 Q424 -4 848 44 L848 140 L0 140 Z" fill="var(--black)"/>
    </svg>
    <svg class="footer-pin" viewBox="0 0 74 108" aria-hidden="true">
      <path d="M37 2 C17 2 2 17 2 37 C2 62 37 106 37 106 C37 106 72 62 72 37 C72 17 57 2 37 2 Z" fill="var(--red)"/>
      <circle cx="37" cy="36" r="14" fill="var(--white)"/>
    </svg>
    <p class="cta">Book your trip today at <span class="url">www.ridemarquel.example</span></p>
  </footer>
</div>
</body>
</html>
```